Loyalty Card

We are a chiropractic and massage practice in Williamsburg, Virginia. We would like to offer our patients a loyalty card for if they buy 7 (60 min) massages then they will get one free. (ex: like a 'punch card'), our staff members would make a special hole punch on the card every time they get an hour massage. We would have to have exclusions listed on the card though as well. (for example: cannot be combined with any other discount or offer. Cannot be combined with insurance, Medicare, auto accident or workmen's compensation claims)

Target Market(s)

Patients of chiropractic office who are currently receiving massage or interested in massage.

Industry/Entity Type

Massage

Colors
eb2027
474747
000000

Requirements
Nice to have
• I included a picture of a screenshot of our current gift card design which I like. It is the front and back of the gift card. It doesn't have any cheesy pictures on it, and looks very professional.
Should not have
• Do not want it to look like a SPA card. It is a professional chiropractic office, although do not want pictures of spines, etc.

```html
<!DOCTYPE html>
<html lang="en">
<head>
<meta charset="utf-8">
<title>Loyalty Card</title>
<link href="https://fonts.googleapis.com/css2?family=Cinzel:wght@700&family=Arimo:wght@400&display=swap" rel="stylesheet">
<style>
  :root {
    --backdrop: #163d4e;
    --card: #ffffff;
    --brand-red: #8b1a1f;
    --ink: #000000;
    --stamp-edge: #9a9a9a;
    --mark-grey: #9b9b9b;
  }
  * { margin: 0; padding: 0; box-sizing: border-box; }
  html, body {
    width: 1200px; height: 1000px; overflow: hidden;
    background: var(--backdrop);
  }
  .loyalty-card {
    position: absolute; left: 75px; top: 180px;
    width: 1050px; height: 640px;
    background: var(--card);
    box-shadow: 0 12px 30px rgba(0,0,0,.35);
    overflow: hidden;
  }
  .brand {
    position: absolute; left: 42px; top: 78px;
    display: flex; align-items: center; gap: 16px;
  }
  .brand-square {
    width: 64px; height: 64px; background: var(--mark-grey);
  }
  .brand-name {
    font-family: "Cinzel", serif; font-weight: 700;
    color: var(--ink); font-size: 26px; line-height: 1;
    letter-spacing: 1px; white-space: nowrap;
  }
  .card-title {
    position: absolute; right: 120px; top: 86px;
    font-family: "Cinzel", serif; font-weight: 700;
    font-size: 44px; color: var(--ink); letter-spacing: 2px;
  }
  .offer {
    position: absolute; left: 0; right: 0; top: 205px;
    text-align: center;
    font-family: "Cinzel", serif; font-weight: 700;
    font-size: 31px; color: var(--ink); letter-spacing: 1.5px;
    word-spacing: 4px;
  }
  .offer-divider { display: inline-block; margin: 0 26px; vertical-align: middle; }
  .punch-grid {
    position: absolute; left: 125px; top: 268px;
    display: grid; grid-template-columns: repeat(4, 92px);
    column-gap: 140px; row-gap: 22px;
  }
  .punch {
    width: 92px; height: 92px;
    background: var(--brand-red);
    border: 2px solid var(--stamp-edge);
    display: flex; align-items: center; justify-content: center;
    font-family: "Cinzel", serif; font-weight: 700;
    color: #fff; font-size: 38px;
  }
  .punch--free { font-size: 24px; }
  .exclusions {
    position: absolute; left: 24px; right: 24px; top: 488px;
    text-align: center;
    font-family: "Arimo", sans-serif; font-size: 23px; line-height: 1.3;
    color: var(--ink);
  }
  .rule-thin {
    position: absolute; left: 0; right: 0; top: 558px; height: 8px;
    background: var(--brand-red);
  }
  .rule-base {
    position: absolute; left: 0; right: 0; top: 582px; height: 58px;
    background: var(--brand-red);
  }
</style>
</head>
<body>
  <article class="loyalty-card">
    <div class="brand">
      <span class="brand-square"></span>
      <span class="brand-name">Ridgeline Chiropractic</span>
    </div>
    <h1 class="card-title">Loyalty Card</h1>
    <p class="offer">Buy Seven 60 Minute Massages<span class="offer-divider"><svg width="16" height="16" viewBox="0 0 16 16"><path d="M8 0 L10 6 L16 8 L10 10 L8 16 L6 10 L0 8 L6 6 Z" fill="#000"/></svg></span>Get One Free</p>
    <div class="punch-grid">
      <div class="punch">1</div>
      <div class="punch">2</div>
      <div class="punch">3</div>
      <div class="punch">4</div>
      <div class="punch">5</div>
      <div class="punch">6</div>
      <div class="punch">7</div>
      <div class="punch punch--free">Free</div>
    </div>
    <p class="exclusions">Cannot be combined with any other discount or offer. Cannot be combined with insurance, Medicare, auto accident or workmen’s compensation claims.</p>
    <div class="rule-thin"></div>
    <div class="rule-base"></div>
  </article>
</body>
</html>
```